Brivane - Business Cards for a new venture

create business card for a startup classified business dealing in construction materials, the cards need to have a professional look but modern, more serious than playful, one of the samples must include the official font (attached), please explore using the official colors in the company's logo

Target Market(s)

Energy sector

Contact Information for Business Card

Font styles to use
Other font styles liked:
• suissnord

Requirements
Must have
• corporate colors (in logo attached)
Nice to have
• Official font (in one of the samples) font is : suissnord
Should not have
• Cartoonish look

```html
<!DOCTYPE html>
<html lang="en">
<head>
<meta charset="utf-8">
<title>Brivane Business Cards</title>
<link rel="stylesheet" href="https://fonts.googleapis.com/css2?family=Michroma&display=swap">
<style>
  :root {
    --backdrop: #212121;
    --card: #ffffff;
    --brand-blue: #1d4a80;
    --brand-grey: #8e8f94;
    --ink: #2b2b2b;
  }
  * { margin: 0; padding: 0; box-sizing: border-box; }
  html, body {
    width: 1200px; height: 1200px; overflow: hidden;
    background: var(--backdrop);
    font-family: "Michroma", sans-serif;
  }
  .card {
    position: absolute; left: 179px; width: 840px; height: 480px;
    background: var(--card); overflow: hidden;
  }
  .card--front { top: 97px; }
  .card--back { top: 633px; }
  .card__band-grey { position: absolute; left: 0; right: 0; top: 466px; height: 6px; background: var(--brand-grey); }
  .card__band-blue { position: absolute; left: 0; right: 0; top: 472px; height: 8px; background: var(--brand-blue); }

  .brand {
    position: absolute; text-align: center; color: var(--brand-grey);
    text-transform: uppercase; white-space: nowrap; line-height: 1.2;
  }
  .card--front .brand { left: 0; right: 0; top: 267px; font-size: 34px; letter-spacing: 3px; }
  .card--back .brand { left: 548px; width: 210px; top: 176px; font-size: 26px; letter-spacing: 2px; }

  .person__name {
    position: absolute; left: 53px; top: 70px;
    font-size: 25px; font-weight: 400; color: var(--brand-blue);
    letter-spacing: 5px; text-transform: uppercase; white-space: nowrap;
  }
  .person__role {
    position: absolute; left: 53px; top: 110px;
    font-size: 11px; color: var(--ink); letter-spacing: 4.5px; text-transform: uppercase; white-space: nowrap;
  }
  .person__email {
    position: absolute; left: 53px; top: 176px; width: 348px;
    font-size: 11px; color: var(--brand-blue); letter-spacing: 2.2px; text-transform: uppercase;
    white-space: nowrap; padding-bottom: 4px; border-bottom: 1.5px solid var(--brand-blue);
  }
  .contact {
    position: absolute; display: flex; align-items: center; gap: 10px;
    font-size: 12px; letter-spacing: 2.4px; color: var(--ink); text-transform: uppercase; white-space: nowrap;
  }
  .contact svg { flex: none; }
  .contact--phone { left: 55px; top: 334px; }
  .contact--office { left: 304px; top: 336px; }
  .contact--address { left: 54px; top: 378px; letter-spacing: 1.2px; }
</style>
</head>
<body>
  <section class="card card--front">
    <div class="brand">Brivane</div>
    <div class="card__band-grey"></div>
    <div class="card__band-blue"></div>
  </section>

  <section class="card card--back">
    <h1 class="person__name">Daniel Harlow</h1>
    <p class="person__role">Associate Manager</p>
    <p class="person__email">danielharlow@northmail.com</p>

    <div class="brand">Brivane</div>

    <div class="contact contact--phone">
      <svg width="13" height="22" viewBox="0 0 13 22" aria-hidden="true">
        <rect x="1" y="1" width="11" height="20" rx="2" fill="none" stroke="#1d4a80" stroke-width="1.4"/>
        <circle cx="6.5" cy="18" r="0.9" fill="#1d4a80"/>
      </svg>
      <span>+62-620457318</span>
    </div>

    <div class="contact contact--office">
      <svg width="17" height="17" viewBox="0 0 17 17" aria-hidden="true">
        <rect x="2" y="1" width="13" height="15" fill="none" stroke="#1d4a80" stroke-width="1.2"/>
        <g fill="#1d4a80">
          <rect x="4" y="3" width="2" height="2"/><rect x="7.5" y="3" width="2" height="2"/><rect x="11" y="3" width="2" height="2"/>
          <rect x="4" y="6.5" width="2" height="2"/><rect x="7.5" y="6.5" width="2" height="2"/><rect x="11" y="6.5" width="2" height="2"/>
          <rect x="7" y="11" width="3" height="5"/>
        </g>
        <line x1="0" y1="16.4" x2="17" y2="16.4" stroke="#1d4a80" stroke-width="1.2"/>
      </svg>
      <span>Brivane Office Building</span>
    </div>

    <div class="contact contact--address">
      <svg width="15" height="20" viewBox="0 0 15 20" aria-hidden="true">
        <path d="M7.5 16 C4 11.5 2 9 2 6.5 a5.5 5.5 0 0 1 11 0 C13 9 11 11.5 7.5 16 Z" fill="none" stroke="#1d4a80" stroke-width="1.2"/>
        <circle cx="7.5" cy="6.5" r="2" fill="none" stroke="#1d4a80" stroke-width="1.2"/>
        <path d="M3 15 L1 19 H14 L12 15" fill="none" stroke="#1d4a80" stroke-width="1.1"/>
      </svg>
      <span>14/18 Marrow Street, Calder Park, Lakeview, CA, 5821094</span>
    </div>

    <div class="card__band-grey"></div>
    <div class="card__band-blue"></div>
  </section>
</body>
</html>
```